Navelock Insurance Solutions Drop Off Flyer

We need a clean, powerful, one page flyer to drop off at businesses. it needs to simple yet needs to jump out for a decision maker to read...

Target Market(s)

Business owners with over 50 employees.....all types of industries...

Industry/Entity Type

Insurance

Font styles to use
Serif
Sans Serif

Colors
0355a3
3176b5
85acd3
ffffff

Requirements
Must have
• You must include all wording on the PDF i included titled Navelock Flyer Idea. Of course, the color and layout is up to you but the wording needs to be included.
Nice to have
• Just a one page Letter size drop off

```html
<!DOCTYPE html>
<html lang="en">
<head>
<meta charset="utf-8">
<title>Navelock Insurance Solutions – Drop Off Flyer</title>
<link rel="stylesheet" href="https://fonts.googleapis.com/css2?family=Oswald:wght@600;700&family=Roboto+Condensed:wght@700;800;900&display=swap">
<style>
  :root {
    --navy: #0355a3;
    --mid-blue: #3176b5;
    --pale-blue: #85acd3;
    --bright-blue: #1fa3f0;
    --sky: #38b4f7;
    --white: #ffffff;
    --ink: #111111;
  }
  * { margin: 0; padding: 0; box-sizing: border-box; }
  html, body { width: 927px; height: 1200px; overflow: hidden; background: var(--white); }
  .flyer {
    position: relative;
    width: 927px;
    height: 1200px;
    overflow: hidden;
    font-family: "Roboto Condensed", "Arial Narrow", sans-serif;
    background: var(--white);
  }
  .hero-photo {
    position: absolute;
    left: 0; top: 0;
    width: 927px; height: 955px;
    background:
      radial-gradient(ellipse at 70% 55%, rgba(49,118,181,0.55) 0%, rgba(3,85,163,0) 55%),
      radial-gradient(ellipse at 20% 75%, rgba(133,172,211,0.35) 0%, rgba(3,85,163,0) 50%),
      linear-gradient(180deg, #0a3f8c 0%, var(--navy) 45%, #0b4d9a 75%, #0a3a80 100%);
  }
  .top-banner {
    position: absolute;
    left: -20px; top: 40px;
    width: 970px; height: 76px;
    background: var(--bright-blue);
    transform: rotate(-2.2deg);
    display: flex; align-items: center; justify-content: center;
  }
  .top-banner p {
    font-family: "Oswald", "Arial Narrow", sans-serif;
    font-weight: 700;
    font-size: 33px;
    color: var(--white);
    letter-spacing: -0.6px;
    text-transform: uppercase;
    white-space: nowrap;
  }
  .headline {
    position: absolute;
    left: 0; top: 182px;
    width: 927px;
    text-align: center;
    color: var(--white);
    font-weight: 800;
    letter-spacing: -1px;
    white-space: nowrap;
  }
  .headline .line { display: block; }
  .headline .lead { font-size: 62px; line-height: 68px; }
  .headline .big-percent {
    font-size: 128px; line-height: 112px;
    color: var(--sky); font-weight: 900; letter-spacing: -4px;
  }
  .headline .next { font-size: 60px; line-height: 64px; }
  .headline .product {
    font-size: 69px; line-height: 74px;
    color: var(--sky); letter-spacing: -2px;
  }
  .headline .close { font-size: 54px; line-height: 94px; }
  .headline .no-cost {
    font-size: 108px; color: var(--sky); font-weight: 900;
    letter-spacing: -4px; vertical-align: -6px;
  }
  .body-copy {
    position: absolute;
    left: 60px; top: 620px;
    width: 505px;
    text-align: center;
    color: var(--white);
    font-weight: 700;
    font-size: 31px;
    line-height: 38px;
    letter-spacing: -0.4px;
    white-space: nowrap;
  }
  .body-copy p + p { margin-top: 36px; }
  .body-copy u {
    text-decoration: underline;
    text-decoration-color: var(--bright-blue);
    text-decoration-thickness: 4px;
    text-underline-offset: 6px;
  }
  .call-badge {
    position: absolute;
    left: 590px; top: 672px;
    width: 300px; height: 210px;
  }
  .footer-band {
    position: absolute;
    left: 0; top: 955px;
    width: 927px; height: 245px;
    background: var(--white);
  }
  .brand {
    position: absolute;
    left: 100px; top: 1035px;
    display: flex; align-items: center; gap: 12px;
  }
  .brand-dot {
    width: 30px; height: 30px; border-radius: 50%;
    background: var(--navy);
  }
  .brand-name {
    font-weight: 800;
    font-size: 34px;
    color: var(--ink);
    letter-spacing: -0.5px;
  }
  .web-address {
    position: absolute;
    left: 88px; top: 1138px;
    font-family: Arial, Helvetica, sans-serif;
    font-size: 27px;
    letter-spacing: 3.6px;
    color: var(--navy);
  }
</style>
</head>
<body>
<main class="flyer">
  <div class="hero-photo" role="img" aria-label="Blue-toned photo of a hand in a suit sleeve fanning out a spread of hundred-dollar bills"></div>

  <div class="top-banner"><p>Read only if you care about your businesses bottom line</p></div>

  <h1 class="headline">
    <span class="line lead">How would you like to pay</span>
    <span class="line big-percent">18% less</span>
    <span class="line next">on your next</span>
    <span class="line product">Workers’ Compensation Renewal</span>
    <span class="line close">at <span class="no-cost">NO COST</span> to you?</span>
  </h1>

  <div class="body-copy">
    <p>In many cases, you <u>DON’T</u> even<br>need to change brokers<br>or insurance companies.</p>
    <p>We are <u>NOT</u> brokers or agents;<br>We are licensed<br>workers’ compensation cost<br>reduction specialists.</p>
  </div>

  <svg class="call-badge" viewBox="0 0 300 210" aria-label="Call us today for a 5-minute overview">
    <g transform="rotate(-9 150 105)">
      <ellipse cx="150" cy="105" rx="140" ry="95" fill="#ffffff"/>
      <ellipse cx="150" cy="105" rx="128" ry="83" fill="#1fa3f0"/>
      <g font-family="Oswald, 'Arial Narrow', sans-serif" font-weight="700" font-size="28" fill="#ffffff" text-anchor="middle">
        <text x="150" y="76">CALL US TODAY</text>
        <text x="150" y="111">FOR A 5-MINUTE</text>
        <text x="150" y="146">OVERVIEW</text>
      </g>
    </g>
  </svg>

  <footer class="footer-band"></footer>
  <div class="brand">
    <span class="brand-dot"></span>
    <span class="brand-name">Navelock Insurance Solutions</span>
  </div>
  <p class="web-address">www.navelock.net</p>
</main>
</body>
</html>
```